Business cards for a tribute and obituary website

Our website is called Quiet Orchard.

It is a special place online for people to remember their loved ones who have passed away, through obituaries and tributes. Friends and family can also convey their condolences on the deceased's memorial page. Celebrating the life of the deceased and remembering their legacy is very important to us – death should not be just about grieving.

We would like the card to look tasteful and modern. The design should ideally not have colours that are too bright. The logo and website URL, www.quietorchardpages.net should be visible on the front of the card, with our slogan "Honouring every life story" on the back.

The design should communicate our purpose – remembering loved ones who have passed – and also a lighter tone of celebrating life. It should not look like a funeral director's card!

Our logo has been attached. Looking forward to some beautiful designs! Get creative :)
Updates

Reason: Thank you all for your designs. The rest of my team and I have not reached a decision on which design to select and I am collecting feedback from them. I will provide feedback for any changes that need to be made soon. It would be great if we could see more original designs and in more colours! We will definitely select a design by this deadline.

Industry/Entity Type

Business

Contact Information for Business Card

Nadia Fenwick
Project Manager
471226809
nadiafenwick@quietorchardpages.net

Font styles to use
Serif
Sans Serif

Requirements
Must have
• Logo and website address (www.quietorchardpages.net) on the front.
Nice to have
• Hi designers! It would be nice to see alternative colours – feel free to try out colours that are tasteful and subtle. The colour of the business card does not have to be the same as the logo.
• We would also like to see the logo used in different ways, perhaps a glossy or embossed finish. The card should look stylish.

```html
<!DOCTYPE html>
<html lang="en">
<head>
<meta charset="utf-8">
<title>Quiet Orchard – Business Cards</title>
<link rel="stylesheet" href="https://fonts.googleapis.com/css2?family=Arvo:wght@400;700&family=Source+Sans+3:wght@400;600&display=swap">
<style>
  :root {
    --navy: #143350;
    --sky: #5aa9dc;
    --ink: #2a3440;
    --muted: #5b6672;
    --card: #ffffff;
    --card-shade: #eef0f2;
    --backdrop: #e7e2da;
  }
  * { box-sizing: border-box; margin: 0; padding: 0; }
  html, body { width: 1200px; height: 885px; overflow: hidden; }
  body {
    background: var(--backdrop);
    font-family: "Source Sans 3", sans-serif;
    color: var(--ink);
    position: relative;
  }
  .card {
    position: absolute;
    width: 560px;
    height: 320px;
    border-radius: 18px;
    background: linear-gradient(135deg, var(--card) 55%, var(--card-shade));
    box-shadow: 0 6px 18px rgba(0,0,0,0.18);
    overflow: hidden;
  }
  .card--front { left: 60px; top: 90px; }
  .card--back { left: 580px; top: 475px; }

  /* front */
  .brand-block {
    position: absolute; left: 0; top: 0; width: 250px; height: 100%;
    display: flex; flex-direction: column; align-items: center; justify-content: center; gap: 16px;
  }
  .brand-dot {
    width: 74px; height: 74px; border-radius: 50%; background: var(--navy);
  }
  .brand-name {
    font-family: "Arvo", serif; font-weight: 700; color: var(--navy);
    font-size: 30px; line-height: 1.05; text-align: center;
  }
  .divider {
    position: absolute; left: 262px; top: 40px; bottom: 40px; width: 1.5px;
    background: linear-gradient(var(--navy), rgba(20,51,80,0.1));
  }
  .person {
    position: absolute; left: 290px; top: 58px; right: 20px;
  }
  .person-name {
    font-family: "Arvo", serif; font-weight: 700; color: var(--navy); font-size: 28px;
  }
  .person-role { font-size: 15px; color: var(--muted); margin-top: 2px; }
  .contact-list { list-style: none; margin-top: 44px; display: flex; flex-direction: column; gap: 9px; }
  .contact-item { display: flex; align-items: center; gap: 9px; font-size: 14px; color: var(--ink); white-space: nowrap; }
  .contact-icon {
    width: 18px; height: 18px; border-radius: 4px; background: var(--navy);
    display: flex; align-items: center; justify-content: center; flex: none;
  }

  /* back */
  .back-brand { position: absolute; left: 60px; top: 70px; display: flex; align-items: center; gap: 22px; }
  .back-brand .brand-dot { width: 96px; height: 96px; }
  .back-name {
    font-family: "Arvo", serif; font-weight: 700; color: var(--navy); font-size: 44px; line-height: 1.0;
  }
  .slogan {
    position: absolute; left: 178px; top: 186px;
    font-family: "Arvo", serif; font-weight: 400; color: var(--sky); font-size: 22px;
  }
  .back-url {
    position: absolute; left: 60px; top: 244px; display: flex; align-items: center; gap: 16px;
    font-family: "Arvo", serif; font-size: 16px; color: var(--ink);
  }
  .back-url-line { width: 80px; height: 1.5px; background: var(--navy); opacity: 0.6; }
</style>
</head>
<body>
  <section class="card card--front" aria-label="Business card front">
    <div class="brand-block">
      <div class="brand-dot"></div>
      <div class="brand-name">Quiet<br>Orchard</div>
    </div>
    <div class="divider"></div>
    <div class="person">
      <h1 class="person-name">Nadia Fenwick</h1>
      <p class="person-role">Project Manager</p>
      <ul class="contact-list">
        <li class="contact-item">
          <span class="contact-icon"><svg width="12" height="12" viewBox="0 0 24 24"><path fill="#fff" d="M6.6 10.8a15 15 0 0 0 6.6 6.6l2.2-2.2a1 1 0 0 1 1-.25 11.4 11.4 0 0 0 3.6.57 1 1 0 0 1 1 1V20a1 1 0 0 1-1 1A17 17 0 0 1 3 4a1 1 0 0 1 1-1h3.5a1 1 0 0 1 1 1c0 1.250.2 2.450.57 3.57a1 1 0 0 1-.25 1z"/></svg></span>
          471226809
        </li>
        <li class="contact-item">
          <span class="contact-icon"><svg width="12" height="12" viewBox="0 0 24 24"><rect x="2" y="5" width="20" height="14" rx="1" fill="none" stroke="#fff" stroke-width="2"/><path d="M2 6l10 7 10-7" fill="none" stroke="#fff" stroke-width="2"/></svg></span>
          nadiafenwick@quietorchardpages.net
        </li>
        <li class="contact-item">
          <span class="contact-icon"><svg width="12" height="12" viewBox="0 0 24 24" fill="none" stroke="#fff" stroke-width="2"><circle cx="12" cy="12" r="9"/><ellipse cx="12" cy="12" rx="4" ry="9"/><path d="M3 12h18"/></svg></span>
          www.quietorchardpages.net
        </li>
      </ul>
    </div>
  </section>

  <section class="card card--back" aria-label="Business card back">
    <div class="back-brand">
      <div class="brand-dot"></div>
      <div class="back-name">Quiet<br>Orchard</div>
    </div>
    <p class="slogan">Honouring every life story</p>
    <div class="back-url"><span>www.quietorchardpages.net</span><span class="back-url-line"></span></div>
  </section>
</body>
</html>
```